Construction Company

I'm a new construction company called Tembrik Construction. I want my card to look simple and clean. I have provided a sample of what I want the front to look like (Tembrik_Card.jpeg) and a back ground for the back of the (Tembrik_Card_Background.jpeg) - the background can be faded so my name and other information is more prominent.
Construction

```html
<!DOCTYPE html>
<html lang="en">
<head>
<meta charset="utf-8">
<title>Tembrik Construction – Business Card</title>
<link href="https://fonts.googleapis.com/css2?family=Mulish:wght@400;500&display=swap" rel="stylesheet">
<style>
  :root {
    --stage: #1d1d1d;
    --card-light: #f5f5f5;
    --card-dark: #3e382b;
    --accent: #e08a1a;
    --text-grey: #6a6a6a;
    --plan-light: #efefef;
    --plan-mid: #e2e2e2;
    --white: #ffffff;
  }
  * { margin: 0; padding: 0; box-sizing: border-box; }
  html, body {
    width: 1200px; height: 900px; overflow: hidden;
    background: var(--stage);
    font-family: "Mulish", sans-serif;
  }
  .card {
    position: absolute;
    left: 354px;
    width: 488px;
    height: 279px;
    overflow: hidden;
  }
  .card-front { top: 153px; background: var(--card-light); }
  .card-back { top: 463px; background: var(--card-dark); }

  .floor-plan {
    position: absolute;
    left: 176px; top: 0;
    width: 312px; height: 279px;
    background: linear-gradient(90deg, var(--card-light) 0%, var(--plan-light) 35%, var(--plan-mid) 100%);
  }

  .person-name {
    position: absolute; left: 30px; top: 37px;
    font-size: 24px; font-weight: 500; color: var(--accent);
    letter-spacing: 0.2px;
  }
  .person-title {
    position: absolute; left: 30px; top: 68px;
    font-size: 14px; font-weight: 400; color: var(--text-grey); letter-spacing: 0.5px;
  }
  .address {
    position: absolute; left: 30px; top: 112px;
    font-size: 14px; line-height: 21px; color: var(--text-grey);
  }
  .contacts {
    position: absolute; left: 30px; top: 172px;
    list-style: none;
  }
  .contacts li {
    display: flex; align-items: center;
    height: 27px;
    font-size: 14px; color: var(--text-grey); letter-spacing: 0.2px;
  }
  .contacts svg { width: 22px; height: 22px; margin-right: 12px; flex: none; }
  .contacts strong { font-weight: 500; }

  .contract-tab {
    position: absolute; right: 0; bottom: 0;
    width: 176px; height: 26px;
    background: var(--card-dark);
    border-top: 3px solid var(--accent);
    border-left: 3px solid var(--accent);
    border-top-left-radius: 18px;
    color: var(--white);
    font-size: 13px; letter-spacing: 1px;
    display: flex; align-items: center; justify-content: center;
    padding-top: 1px;
  }

  .brand {
    position: absolute; left: 0; right: 0; top: 0; bottom: 0;
    display: flex; align-items: center; justify-content: center;
    gap: 14px;
    color: var(--accent);
    font-size: 34px; font-weight: 500; letter-spacing: 0.5px;
  }
  .brand-mark {
    width: 18px; height: 18px;
    background: var(--accent);
    flex: none;
  }
</style>
</head>
<body>
  <section class="card card-front" aria-label="Card front">
    <div class="floor-plan" role="img" aria-label="Faded architectural floor plan background"></div>

    <h1 class="person-name">Marcelo Quintana</h1>
    <p class="person-title">OWNER</p>
    <p class="address">4820 Cedar Ridge Lane<br>Fresno, CA 93711</p>

    <ul class="contacts">
      <li>
        <svg viewBox="0 0 22 22" aria-hidden="true">
          <circle cx="11" cy="11" r="11" fill="var(--accent)"/>
          <rect x="7.5" y="5" width="7" height="12" rx="1.2" fill="none" stroke="var(--white)" stroke-width="1.5"/>
          <line x1="10" y1="15" x2="12" y2="15" stroke="var(--white)" stroke-width="1.2"/>
        </svg>
        555.210.3380
      </li>
      <li>
        <svg viewBox="0 0 22 22" aria-hidden="true">
          <circle cx="11" cy="11" r="11" fill="var(--accent)"/>
          <rect x="5.5" y="7" width="11" height="8" fill="var(--white)"/>
          <polyline points="5.5,7 11,11.5 16.5,7" fill="none" stroke="var(--accent)" stroke-width="1.2"/>
        </svg>
        marcelo@tembrikconstruction.com
      </li>
      <li>
        <svg viewBox="0 0 22 22" aria-hidden="true">
          <circle cx="11" cy="11" r="11" fill="var(--accent)"/>
          <circle cx="11" cy="11" r="6" fill="none" stroke="var(--white)" stroke-width="1.5"/>
          <ellipse cx="11" cy="11" rx="2.6" ry="6" fill="none" stroke="var(--white)" stroke-width="1.2"/>
          <line x1="5" y1="11" x2="17" y2="11" stroke="var(--white)" stroke-width="1.2"/>
        </svg>
        <span>www.<strong>tembrikconstruction</strong>.com</span>
      </li>
    </ul>

    <div class="contract-tab">CONTRACT #471296</div>
  </section>

  <section class="card card-back" aria-label="Card back">
    <p class="brand">
      <span class="brand-mark" aria-hidden="true"></span>
      <span class="brand-name">Tembrik Construction</span>
    </p>
  </section>
</body>
</html>
```